Redesign web application

we are a tele health start up. we need a new design for our platform that allows users, their family and docs to access their detailed stats online
users take readings using our wireless devices that transmit the readings to our server in the background All this happens in real time . and users can instantly login to the portal to view readings , make comments, , view charts,
if readings are not within in prescribed thresholds then alerts are reported on the website, SMS and email
please see the screenshots of existing pages
We need the following pages re designed
login page
patient DB summary , patient DB condition
Doc DB
Nurse DB
After you submit designs and we choose the winning design . please help to make minor modifications after that so that we can use it
Target Market(s)
Paying
Doctors/ Clinics/Clinic chains/ Specialists will be the ones who are paying for the service. the service
Non Paying
patients family members, doctors all will be accessing the system to view readings, alerts , make comments , see charts
Industry/Entity Type
Health
Colors
Look and feel

```html
<!DOCTYPE html>
<html lang="en">
<head>
<meta charset="utf-8">
<title>VitaLink – Patient DB Summary</title>
<link href="https://fonts.googleapis.com/css2?family=Lato:ital,wght@0,400;0,700;1,400;1,700&family=Ubuntu:ital,wght@0,400;0,500;1,400;1,500&display=swap" rel="stylesheet">
<style>
:root{
  --blue:#5ba3d3;
  --green:#8cc63f;
  --text:#222;
  --muted:#999;
  --link:#4a9fd8;
  --panel:#efefef;
  --line:#d8d8d8;
  --dark:#353535;
  --navtext:#fff;
}
*{box-sizing:border-box;margin:0;padding:0}
html,body{width:1200px;height:1023px;overflow:hidden;background:#fff}
body{position:relative;font-family:"Lato",sans-serif;color:var(--text)}
.abs{position:absolute}

.header{position:absolute;left:0;top:0;width:1200px;height:62px;background:linear-gradient(#fafafa,#ececec);border-bottom:1px solid #ddd}
.brand{position:absolute;left:174px;top:13px;font-size:27px;font-weight:700;color:#111;letter-spacing:.5px;display:flex;align-items:center;gap:7px}
.brand .sq{width:14px;height:14px;border:2px solid #3a4fc7}
.search{position:absolute;left:581px;top:21px;width:220px;height:24px;border:1px solid #ccc;border-radius:12px;background:#fff;font-size:13px;color:#bbb;padding:4px 15px}
.search svg{position:absolute;right:10px;top:4px}
.vdivider{position:absolute;left:822px;top:0;width:1px;height:62px;background:#d6d6d6}
.contact{position:absolute;font-size:12px;color:#444;display:flex;align-items:center;gap:10px}

.nav{position:absolute;left:0;top:62px;width:1200px;height:36px;background:var(--blue);display:flex}
.nav a{display:flex;align-items:center;justify-content:center;color:var(--navtext);font-weight:700;font-size:14px;text-decoration:none;border-right:1px solid #80b9de;height:36px;position:relative}
.nav a.active{background:var(--green)}
.nav a.active::after{content:"";position:absolute;bottom:0;left:50%;margin-left:-4px;border:4px solid transparent;border-bottom-color:#fff}

.tab{position:absolute;top:132px;height:27px;border:1px solid #d0d0d0;border-bottom:none;background:linear-gradient(#fff,#f2f2f2);font-size:14px;color:var(--link);display:flex;align-items:center;justify-content:center}
.tab.current{background:#f0f0f0;color:#222;height:28px}
.info{position:absolute;left:171px;top:159px;width:858px;height:172px;border:1px solid #d0d0d0;background:repeating-linear-gradient(135deg,#fbfbfb 0 3px,#f3f3f3 3px 5px)}
.photo{position:absolute;left:172px;top:171px;width:111px;height:132px;background:linear-gradient(#c8cbd3,#9aa1ad)}
.lbl{position:absolute;font-size:12.5px;color:#222}
.val{position:absolute;font-size:12.5px;color:var(--muted)}
.lnk{position:absolute;font-size:12.5px;color:var(--link)}
.r{text-align:right}

.side{position:absolute;left:171px;top:352px;width:136px;height:239px;background:#f1f1f1;box-shadow:0 1px 3px rgba(0,0,0,.2)}
.side .item{height:34px;border-bottom:1px solid #e3e3e3;display:flex;align-items:center;gap:10px;padding-left:8px;font-size:14px;color:#333;background:linear-gradient(#fafafa,#eee)}
.side .item:first-child{margin-top:11px}

.widget{position:absolute;left:341px;width:325px;height:169px;background:var(--panel);border-radius:8px;overflow:hidden}
.widget .head{height:42px;border-bottom:4px solid var(--blue);display:flex;align-items:center;padding-left:21px;font-weight:700;font-size:14px;position:relative}
.widget .tools{position:absolute;right:28px;top:16px;display:flex;gap:16px}
.widget .row{height:25px;border-bottom:1px solid #e0e0e0;font-size:11.5px;display:flex;align-items:center;justify-content:center}
.widget .row:first-of-type{height:30px}

.feed{position:absolute;left:685px;top:356px;width:344px;height:565px;background:var(--panel);border-radius:8px;overflow:hidden;font-family:"Ubuntu",sans-serif;font-size:10px;color:#333}
.entry{position:absolute;left:0;width:344px}
.avatar{position:absolute;left:1px;top:6px;width:31px;height:31px;border-radius:3px;background:linear-gradient(#fff,#c9c9c9);border:1px solid #bbb}
.entry .body{margin-left:34px;width:306px}
.meta{font-style:italic;color:#444;height:14px;line-height:14px;margin-top:1px}
.etitle{font-style:italic;font-weight:500;color:#222;margin-top:15px;border-bottom:1px solid #c7c7c7;padding-bottom:2px;line-height:13px}
.etext{border-bottom:1px solid #c7c7c7;padding:7px 0 3px;line-height:12px}
.reading{padding-top:6px;line-height:14px;color:#444}

.footer-line{position:absolute;left:0;top:955px;width:1200px;height:4px;background:var(--blue)}
.footer{position:absolute;left:0;top:959px;width:1200px;height:64px;background:var(--dark);color:#eee;font-size:12.5px}
.footer .copy{position:absolute;left:175px;top:22px}
.social{position:absolute;right:172px;top:22px;display:flex;gap:11px}
.social span{width:17px;height:17px;border-radius:50%;background:#888}
</style>
</head>
<body>

<header class="header">
  <div class="brand">VitaLink <span class="sq"></span></div>
  <div class="search">Search:
    <svg width="15" height="15" viewBox="0 0 15 15"><circle cx="6" cy="6" r="4.5" fill="none" stroke="#111" stroke-width="2"/><line x1="9.5" y1="9.5" x2="13.5" y2="13.5" stroke="#111" stroke-width="2.2"/></svg>
  </div>
  <div class="vdivider"></div>
  <div class="contact" style="left:864px;top:14px">
    <svg width="12" height="12" viewBox="0 0 12 12"><path d="M2 1l2 0 1 3-1.5 1a7 7 0 0 0 3.5 3.5l1-1.5 3 1v2c0 1-1 1.5-2 1.5A10 10 0 0 1 .5 3C.5 2 1 1 2 1z" fill="var(--blue)"/></svg>
    <span>Care Hotline (6100 2200)</span>
  </div>
  <div class="contact" style="left:843px;top:34px">
    <svg width="15" height="11" viewBox="0 0 15 11"><rect x=".75" y=".75" width="13.5" height="9.5" fill="none" stroke="var(--blue)" stroke-width="1.5"/><path d="M1 1l6.5 5 6.5-5" fill="none" stroke="var(--blue)" stroke-width="1.5"/></svg>
    <span>support@vitalink.care</span>
  </div>
</header>

<nav class="nav">
  <a style="width:306px">DashBoard</a>
  <a class="active" style="width:225px">Patient DB Summary</a>
  <a style="width:222px">Patient DB Condition</a>
  <a style="width:162px">Doc DB</a>
  <a style="width:285px;border-right:none">Nurse DB</a>
</nav>

<div class="tab current" style="left:171px;width:109px">Summary</div>
<div class="tab" style="left:284px;width:109px">Blood Pressure</div>
<div class="tab" style="left:395px;width:111px">Blood Glucose</div>
<div class="tab" style="left:508px;width:109px">Body Weight</div>

<section class="info"></section>
<div class="photo" role="img" aria-label="Patient portrait photo"></div>

<div class="lbl" style="left:325px;top:181px">Name of the Patient:</div>
<div class="abs" style="left:460px;top:181px;font-size:12.5px;font-weight:700;color:var(--green)">Tan Wei Ming</div>
<svg class="abs" style="left:597px;top:183px" width="12" height="11" viewBox="0 0 12 11"><rect x=".5" y="2.5" width="8" height="8" fill="none" stroke="var(--link)"/><path d="M5 7l1-2.5L10.5 0 12 1.5 7.5 6z" fill="var(--link)"/></svg>
<div class="lbl" style="left:325px;top:207px">Add General comment</div>
<div class="abs" style="left:459px;top:205px;width:150px;height:22px;border:1px solid #d5d5d5;background:#fff"></div>
<div class="val" style="left:325px;top:240px">12A Orchard Lane Singapore 238801</div>
<div class="lbl r" style="left:325px;top:260px;width:108px">Phone #:</div>
<div class="val" style="left:446px;top:260px">61234567</div>
<div class="lbl r" style="left:325px;top:277px;width:108px">Age:</div>
<div class="val" style="left:446px;top:277px">57</div>
<div class="lbl r" style="left:300px;top:294px;width:133px">Preferred Language:</div>
<div class="val" style="left:446px;top:294px">Chinese</div>

<div class="lbl r" style="left:620px;top:182px;width:86px">NRIC #:</div>
<div class="lnk" style="left:720px;top:182px">S5678K</div>
<div class="lbl r" style="left:620px;top:204px;width:86px">Contact #:</div>
<div class="lnk" style="left:720px;top:204px;line-height:15px">91234567 (HP),<br>61234567 (H/O)</div>
<div class="lbl r" style="left:620px;top:240px;width:86px;line-height:15px">Patient of<br>Dept(s):</div>
<div class="lnk" style="left:720px;top:240px">Cardio-AMI, UAT1</div>

<div class="lbl" style="left:863px;top:182px">Activated on:</div>
<div class="lnk" style="left:947px;top:182px">07-Apr-2014</div>
<div class="lbl" style="left:863px;top:205px">First Reading:</div>
<div class="lnk" style="left:947px;top:205px">15-Apr-2014</div>
<div class="lbl" style="left:863px;top:228px">Last Reading:</div>
<div class="lnk" style="left:947px;top:228px">26-May-2014</div>

<aside class="side">
  <div class="item"><svg width="16" height="10" viewBox="0 0 16 10"><path d="M2 9a6 6 0 0 1 12 0" fill="none" stroke="#333" stroke-width="2.2"/><line x1="8" y1="9" x2="11" y2="4" stroke="#333" stroke-width="2"/></svg>Site Usage</div>
  <div class="item"><svg width="16" height="11" viewBox="0 0 16 11"><rect width="15" height="11" rx="1" fill="#333"/><path d="M0 1l7.5 5L15 1" fill="none" stroke="#eee" stroke-width="1.2"/></svg>Email</div>
  <div class="item"><svg width="16" height="13" viewBox="0 0 16 13"><rect x="6" y="0" width="4" height="4" fill="#333"/><rect x="0" y="9" width="4" height="4" fill="#333"/><rect x="6" y="9" width="4" height="4" fill="#333"/><rect x="12" y="9" width="4" height="4" fill="#333"/><path d="M8 4v5M2 9V6.5h12V9" fill="none" stroke="#333" stroke-width="1.3"/></svg>Doctors DB</div>
  <div class="item"><svg width="16" height="14" viewBox="0 0 16 14"><circle cx="6" cy="8" r="4" fill="none" stroke="#333" stroke-width="2.5" stroke-dasharray="2 1.2"/><circle cx="12.5" cy="3.5" r="2.5" fill="none" stroke="#333" stroke-width="1.8"/></svg>Settings</div>
  <div class="item"><svg width="16" height="13" viewBox="0 0 16 13"><rect x=".75" y=".75" width="14.5" height="11.5" fill="none" stroke="#333" stroke-width="1.5"/><rect x="4" y="5" width="2" height="6" fill="#333"/><rect x="7" y="3" width="2" height="8" fill="#333"/><rect x="10" y="6" width="2" height="5" fill="#333"/></svg>View Chart</div>
  <div class="item"><svg width="16" height="14" viewBox="0 0 16 14"><path d="M4.5 3.5a5.5 5.5 0 1 0 7 0" fill="none" stroke="#333" stroke-width="2"/><line x1="8" y1="0" x2="8" y2="7" stroke="#333" stroke-width="2"/></svg>Logout</div>
</aside>

<section class="widget" style="top:356px">
  <div class="head">Blood Pressure
    <div class="tools">
      <svg width="11" height="11" viewBox="0 0 11 11"><path d="M9.5 4A4 4 0 0 0 2 3M1.5 7A4 4 0 0 0 9 8" fill="none" stroke="#222" stroke-width="1.6"/><path d="M1 0v4h4zM10 11V7H6z" fill="#222"/></svg>
      <svg width="12" height="12" viewBox="0 0 12 12"><rect x=".5" y="1.5" width="11" height="10" fill="none" stroke="#222"/><rect x=".5" y="1.5" width="11" height="3" fill="#222"/><path d="M4 5v6M8 5v6M1 8h10" stroke="#222" stroke-width=".8"/></svg>
      <svg width="9" height="9" viewBox="0 0 9 9"><path d="M1 1l7 7M8 1L1 8" stroke="#222" stroke-width="2.2"/></svg>
    </div>
  </div>
  <div class="row">No Data Available</div><div class="row"></div><div class="row"></div>
</section>

<section class="widget" style="top:554px">
  <div class="head">Blood Glucose
    <div class="tools">
      <svg width="11" height="11" viewBox="0 0 11 11"><path d="M9.5 4A4 4 0 0 0 2 3M1.5 7A4 4 0 0 0 9 8" fill="none" stroke="#222" stroke-width="1.6"/><path d="M1 0v4h4zM10 11V7H6z" fill="#222"/></svg>
      <svg width="12" height="12" viewBox="0 0 12 12"><rect x=".5" y="1.5" width="11" height="10" fill="none" stroke="#222"/><rect x=".5" y="1.5" width="11" height="3" fill="#222"/><path d="M4 5v6M8 5v6M1 8h10" stroke="#222" stroke-width=".8"/></svg>
      <svg width="9" height="9" viewBox="0 0 9 9"><path d="M1 1l7 7M8 1L1 8" stroke="#222" stroke-width="2.2"/></svg>
    </div>
  </div>
  <div class="row">No Data Available</div><div class="row"></div><div class="row"></div>
</section>

<section class="widget" style="top:752px">
  <div class="head">Body Weight
    <div class="tools">
      <svg width="11" height="11" viewBox="0 0 11 11"><path d="M9.5 4A4 4 0 0 0 2 3M1.5 7A4 4 0 0 0 9 8" fill="none" stroke="#222" stroke-width="1.6"/><path d="M1 0v4h4zM10 11V7H6z" fill="#222"/></svg>
      <svg width="12" height="12" viewBox="0 0 12 12"><rect x=".5" y="1.5" width="11" height="10" fill="none" stroke="#222"/><rect x=".5" y="1.5" width="11" height="3" fill="#222"/><path d="M4 5v6M8 5v6M1 8h10" stroke="#222" stroke-width=".8"/></svg>
      <svg width="9" height="9" viewBox="0 0 9 9"><path d="M1 1l7 7M8 1L1 8" stroke="#222" stroke-width="2.2"/></svg>
    </div>
  </div>
  <div class="row">No Data Available</div><div class="row"></div><div class="row"></div>
</section>

<section class="feed">
  <div class="entry" style="top:3px">
    <div class="avatar" role="img" aria-label="Nurse avatar"></div>
    <div class="body">
      <div class="meta">UAT NURSE on Jun 05 11:05 AM</div>
      <div class="etitle">General Comments - General</div>
      <div class="etext">helow..wsdfsdf</div>
    </div>
  </div>
  <div class="entry" style="top:100px">
    <div class="avatar" role="img" aria-label="Nurse avatar"></div>
    <div class="body">
      <div class="meta">UAT NURSE on Jun 05 11:05 AM</div>
      <div class="etitle">Observation Comments - Blood Pressure</div>
      <div class="etext">helow.r</div>
      <div class="reading">25-May-2014 9:44 PM<br>Blood Pressure - Systolic: 106 mmHg Diastolic: 72 mmHg Pulse: 84 Beat/min</div>
    </div>
  </div>
  <div class="entry" style="top:230px">
    <div class="avatar" role="img" aria-label="Nurse avatar"></div>
    <div class="body">
      <div class="meta">UAT NURSE on Jun 05 11:04 AM</div>
      <div class="etitle">Observation Comments - Blood Pressure</div>
      <div class="etext">ge go</div>
      <div class="reading">26-May-2014 12:19 AM<br>Blood Pressure - Systolic: 117 mmHg Diastolic: 50 mmHg Pulse: 103 Beat/min</div>
    </div>
  </div>
  <div class="entry" style="top:360px">
    <div class="avatar" role="img" aria-label="Nurse avatar"></div>
    <div class="body">
      <div class="meta">UAT NURSE on Jun 05 10:35 AM</div>
      <div class="etitle">Observation Comments - Blood Pressure</div>
      <div class="etext">sdfsfds</div>
      <div class="reading">26-May-2014 2:53 PM<br>Blood Pressure - Systolic: 109 mmHg Diastolic: 78 mmHg Pulse: 83 Beat/min</div>
    </div>
  </div>
  <div class="entry" style="top:489px">
    <div class="avatar" role="img" aria-label="Nurse avatar"></div>
    <div class="body">
      <div class="meta">UAT NURSE on Jun 05 10:24 AM</div>
      <div class="etitle">Observation Comments - Blood Pressure</div>
      <div class="etext">add new observation comment</div>
    </div>
  </div>
</section>

<div class="footer-line"></div>
<footer class="footer">
  <div class="copy">© 2014 vitalink.care All Rights reserved</div>
  <div class="social"><span></span><span></span><span></span><span></span></div>
</footer>

</body>
</html>
```